Orvella Aid Fund - New Website Design

I need a site that looks like this http://renwick-gives-now.org for boat donations. So please replace the cars with boats.

```html
<!DOCTYPE html>
<html lang="en">
<head>
<meta charset="UTF-8">
<title>Orvella Aid Fund – Donate Boat to Charity</title>
<link href="https://fonts.googleapis.com/css2?family=Roboto:wght@300;400;500;700&display=swap" rel="stylesheet">
<style>
  :root{
    --blue:#4a6fb8;
    --blue-dark:#3d5ea0;
    --red:#f2675a;
    --ink:#333a44;
    --muted:#7b818a;
    --line:#e3e6ea;
    --soft:#f4f5f7;
    --white:#ffffff;
  }
  *{box-sizing:border-box;margin:0;padding:0}
  html,body{width:1200px;height:2620px;overflow:hidden}
  body{position:relative;font-family:"Roboto",Arial,sans-serif;color:var(--ink);background:var(--white)}

  /* header */
  .site-header{position:absolute;left:0;top:0;width:1200px;height:120px;background:var(--white)}
  .brand{position:absolute;left:92px;top:38px;font-size:36px;font-weight:700;color:var(--ink)}
  .call{position:absolute;left:740px;top:32px;display:flex;align-items:center;gap:14px}
  .call-icon{width:46px;height:46px;border-radius:50%;background:var(--red);display:flex;align-items:center;justify-content:center}
  .call-text{font-size:15px;color:var(--muted);line-height:1.2}
  .call-text strong{display:block;font-size:19px;color:var(--ink);font-weight:700}
  .btn{display:inline-block;background:var(--blue);color:var(--white);font-size:14px;font-weight:500;border-radius:4px;text-align:center}
  .header-cta{position:absolute;left:950px;top:34px;width:160px;height:42px;line-height:42px}

  /* nav */
  .main-nav{position:absolute;left:0;top:120px;width:1200px;height:40px;background:var(--blue)}
  .main-nav ul{list-style:none;display:flex;margin-left:96px;height:40px}
  .main-nav li{padding:0 26px;line-height:40px;font-size:13px;font-weight:500;color:var(--white);letter-spacing:.5px}
  .main-nav li.active{background:var(--red)}

  /* hero */
  .hero{position:absolute;left:0;top:160px;width:1200px;height:500px;background:linear-gradient(90deg,#dcdfe4 0%,#eef0f3 45%,#f6f7f9 100%)}
  .hero-photo{position:absolute;left:0;top:0;width:360px;height:500px;background:linear-gradient(135deg,#c9b9ad 0%,#a9b3c4 55%,#7e90b3 100%)}
  .hero-title{position:absolute;left:372px;top:190px;width:300px;font-size:42px;font-weight:400;color:var(--red);line-height:1.15;text-align:center}
  .hero-sub{position:absolute;left:372px;top:300px;width:300px;font-size:17px;font-weight:500;text-align:center}

  .pickup-form{position:absolute;left:688px;top:60px;width:424px;height:550px;background:var(--red);padding:22px 26px;clip-path:polygon(0 0,100% 0,100% 95%,50% 100%,0 95%);color:var(--white)}
  .pickup-form h2{font-size:30px;font-weight:400;text-align:center;margin-bottom:14px}
  .pickup-form h3{font-size:15px;font-weight:500;margin:10px 0 10px}
  .field-row{display:flex;gap:14px;margin-bottom:12px}
  .field{flex:1;height:36px;background:var(--white);border-radius:3px;color:#9aa0a8;font-size:12px;line-height:36px;padding-left:10px}
  .field.select::after{content:"▾";float:right;margin-right:10px;color:#666}
  .form-submit{display:block;margin:18px auto 0;width:170px;height:42px;line-height:42px}

  /* welcome */
  .welcome{position:absolute;left:0;top:660px;width:1200px;height:360px;background:var(--soft);text-align:center}
  .section-title{font-size:30px;font-weight:400;color:var(--ink);letter-spacing:1px}
  .rule{width:80px;height:2px;background:var(--red);margin:14px auto}
  .welcome .section-title{margin-top:100px}
  .welcome p{width:740px;margin:8px auto 0;font-size:13px;line-height:1.7;color:var(--muted)}
  .welcome .btn{margin-top:34px;width:130px;height:40px;line-height:40px}

  /* steps */
  .steps{position:absolute;left:0;top:1020px;width:1200px;height:820px;background:var(--white)}
  .steps .section-title{position:absolute;top:94px;width:1200px;text-align:center}
  .steps .tagline{position:absolute;top:138px;width:1200px;text-align:center;font-size:16px;font-weight:500}
  .step{position:absolute;background:var(--blue);color:var(--white);text-align:center;font-size:14px;line-height:1.4;display:flex;flex-direction:column;align-items:center}
  .step.down{clip-path:polygon(0 0,100% 0,100% 62%,50% 100%,0 62%);justify-content:flex-start;padding-top:28px}
  .step.up{clip-path:polygon(50% 0,100% 38%,100% 100%,0 100%,0 38%);justify-content:flex-end;padding-bottom:26px}
  .step.accent{background:var(--red)}
  .step-icon{width:58px;height:58px;border-radius:50%;background:var(--white);display:flex;align-items:center;justify-content:center}
  .step.down .step-icon{margin-top:16px}
  .step.up .step-icon{margin-bottom:14px}

  /* faq */
  .faq{position:absolute;left:0;top:1840px;width:1200px;height:640px;background:linear-gradient(120deg,#3e3a3b 0%,#5a5150 45%,#8a5e5c 80%,#b0524c 100%)}
  .faq .section-title{color:var(--white);text-align:center;margin-top:86px}
  .faq-list{position:absolute;left:280px;top:160px;width:640px}
  .faq-open{background:var(--white);border-radius:4px;padding:18px 60px 18px 26px;position:relative;height:112px}
  .faq-open h4{font-size:17px;font-weight:500;color:var(--red);margin-bottom:8px}
  .faq-open p{font-size:12px;color:var(--muted);line-height:1.6}
  .faq-open .toggle{position:absolute;right:18px;top:22px}
  .faq-item{margin-top:10px;height:34px;background:var(--white);border-radius:3px;padding:0 14px;display:flex;align-items:center;justify-content:space-between;font-size:12px;color:var(--ink)}
  .faq-item .dot{width:16px;height:16px;border-radius:50%;background:var(--blue);color:var(--white);font-size:12px;line-height:16px;text-align:center}

  /* footer */
  .site-footer{position:absolute;left:0;top:2480px;width:1200px;height:140px;background:var(--white);text-align:center}
  .site-footer ul{list-style:none;display:flex;justify-content:center;gap:62px;margin-top:44px;font-size:13px;font-weight:500}
  .site-footer li.active{color:var(--red)}
  .site-footer hr{border:0;border-top:1px solid var(--line);width:1060px;margin:26px auto 20px}
  .copyright{font-size:12px;color:var(--muted)}
  .to-top{position:absolute;left:1110px;top:66px;width:36px;height:36px;border-radius:50%;background:var(--red)}
</style>
</head>
<body>

<header class="site-header">
  <div class="brand">Logo Here</div>
  <div class="call">
    <div class="call-icon">
      <svg width="22" height="22" viewBox="0 0 24 24"><path fill="#fff" d="M6.6 10.8a15.1 15.1 0 0 0 6.6 6.6l2.2-2.2c.3-.3.7-.4 1-.2 1.1.4 2.3.6 3.6.6.6 0 1 .4 1 1V20c0 .6-.4 1-1 1A17 17 0 0 1 3 4c0-.6.4-1 1-1h3.5c.6 0 1 .4 1 1 0 1.3.2 2.5.6 3.6.1.3 0 .7-.2 1z"/></svg>
    </div>
    <div class="call-text">Call Now :<strong>1-555-014-2290</strong></div>
  </div>
  <span class="btn header-cta">Donate Now</span>
</header>

<nav class="main-nav">
  <ul>
    <li class="active">HOME</li>
    <li>ABOUT US</li>
    <li>GET STARTED</li>
    <li>CONTACT US</li>
  </ul>
</nav>

<section class="hero">
  <div class="hero-photo" role="img" aria-label="Photo of a smiling older couple embracing"></div>
  <h1 class="hero-title">Donate Boat to Charity!</h1>
  <p class="hero-sub">Your car boat can make a difference!</p>

  <form class="pickup-form">
    <h2>Donation Pick Up Form</h2>
    <h3>Contact Information</h3>
    <div class="field-row"><div class="field">First Name</div><div class="field">Last Name</div></div>
    <div class="field-row"><div class="field">Zip Code</div><div class="field">Best Phone</div></div>
    <div class="field-row"><div class="field">Email Address</div></div>
    <h3>Boat Donation Information</h3>
    <div class="field-row"><div class="field select">Choose Year</div><div class="field select">Choose Make</div></div>
    <div class="field-row"><div class="field">Model of Boat</div></div>
    <span class="btn form-submit">Submit Application</span>
  </form>
</section>

<section class="welcome">
  <h2 class="section-title">WELCOME TO COMPANY</h2>
  <div class="rule"></div>
  <p>Lorem ipsum dolor sit amet, consectetur adipiscing elit. Aenean commodo ligula eget dolor aenean massa cum sociis natoque penatibus et magnis dis parturient montes, nascetur ridiculus mus. Donec quam felis ultricies nec pellentesque eu pretium quis sem.</p>
  <span class="btn">Read more</span>
</section>

<section class="steps">
  <h2 class="section-title">DONATE BOAT TO CHARITY!</h2>
  <p class="tagline">Your boat can make a difference!</p>

  <div class="step down" style="left:228px;top:200px;width:200px;height:190px">
    Free Towing in<br>24-48 Hours
    <div class="step-icon"><svg width="34" height="34" viewBox="0 0 34 34"><path fill="#4a6fb8" d="M3 20h18v-8h6l4 6v2h-3v2H3z"/><circle cx="9" cy="24" r="3" fill="#4a6fb8"/><circle cx="25" cy="24" r="3" fill="#4a6fb8"/></svg></div>
  </div>
  <div class="step down" style="left:488px;top:200px;width:224px;height:190px">
    Boat Donations Help Fund<br>Charitable Programs
    <div class="step-icon"><svg width="32" height="32" viewBox="0 0 24 24"><path fill="#4a6fb8" d="M12 21 4 13a5 5 0 0 1 8-6 5 5 0 0 1 8 6z"/></svg></div>
  </div>
  <div class="step down" style="left:760px;top:200px;width:200px;height:190px">
    We Accept<br>All Boats
    <div class="step-icon"><svg width="34" height="34" viewBox="0 0 34 34"><path fill="#4a6fb8" d="M16 6v14H7zM18 9l8 11h-8zM4 22h26l-4 6H8z"/></svg></div>
  </div>

  <div class="step up" style="left:360px;top:360px;width:210px;height:190px">
    <div class="step-icon"><svg width="32" height="32" viewBox="0 0 24 24"><path fill="#4a6fb8" d="M5 12l4 4 10-10 2 2L9 20l-6-6z"/></svg></div>
    Hassle<br>Free Donation
  </div>
  <div class="step up" style="left:628px;top:360px;width:210px;height:190px">
    <div class="step-icon"><svg width="32" height="32" viewBox="0 0 24 24"><path fill="#4a6fb8" d="M4 4h10l6 6-10 10-6-6zM8 7a1.5 1.5 0 1 0 0 3 1.5 1.5 0 0 0 0-3z"/></svg></div>
    Boat Will be Sold on the<br>Largest Auction Network
  </div>

  <div class="step up accent" style="left:500px;top:540px;width:200px;height:180px">
    Receive<br>Tax Deduction
    <div class="step-icon" style="margin:12px 0 0"><svg width="30" height="30" viewBox="0 0 24 24"><path fill="#f2675a" d="M5 3h14v18l-3-2-2 2-2-2-2 2-2-2-3 2zM8 7v2h8V7zm0 4v2h8v-2z"/></svg></div>
  </div>
</section>

<section class="faq" role="img" aria-label="Soft-focus photo of hands holding a red heart">
  <h2 class="section-title">FREQUENTLY ASKED QUESTIONS</h2>
  <div class="rule"></div>
  <div class="faq-list">
    <div class="faq-open">
      <h4>What types of vehicles can be donated?</h4>
      <p>Lorem ipsum dolor sit amet consectetur adipiscing elit. Aenean commodo ligula eget dolor aenean massa.</p>
      <svg class="toggle" width="26" height="26" viewBox="0 0 26 26"><circle cx="13" cy="13" r="12" fill="#f2675a"/><path d="M8 13h10" stroke="#fff" stroke-width="2.5"/></svg>
    </div>
    <div class="faq-item">What paperwork do I need to donate my vehicle?<span class="dot">+</span></div>
    <div class="faq-item">Is my donation tax deductible?<span class="dot">+</span></div>
    <div class="faq-item">What if the vehicle is not registered in my name?<span class="dot">+</span></div>
    <div class="faq-item">How much will I receive as a tax deduction for my vehicle?<span class="dot">+</span></div>
    <div class="faq-item">When will I receive my tax receipt?<span class="dot">+</span></div>
    <div class="faq-item">How do I schedule a pick-up?<span class="dot">+</span></div>
  </div>
</section>

<footer class="site-footer">
  <ul>
    <li class="active">HOME</li>
    <li>ABOUT US</li>
    <li>GET STARTED</li>
    <li>CONTACT US</li>
  </ul>
  <hr>
  <p class="copyright">Copyright 2017 - All Rights Reserved</p>
  <div class="to-top"></div>
</footer>

</body>
</html>
```